Church Invite (Business Sized)

I would like to get a design for a church invite card. The design should be able to be used on business sized cards. The front should include the "Zephra" logo provided with the phrase "You're Welcomed Here". The back should include the church logo, name, address, phone number, and website.

Church Name: Morningbrook Restoration Chapel
Church Address: 1187 Tollgate Lane, Decatur, GA, 30871
Church Number: 555-017-3926
Church Website: www.mrcministry.example

```html
<!DOCTYPE html>
<html lang="en">
<head>
<meta charset="utf-8">
<title>Morningbrook Restoration Chapel – Invite Card</title>
<link rel="stylesheet" href="https://fonts.googleapis.com/css2?family=Montserrat:wght@300;400;500;700;800&display=swap">
<style>
  :root {
    --backdrop: #d9d9db;
    --card: #f3f3f4;
    --royal: #1565c0;
    --cyan: #00b2d6;
    --charcoal: #2d2d30;
    --ink: #2a2a2c;
    --white: #ffffff;
  }
  * { margin: 0; padding: 0; box-sizing: border-box; }
  html, body { width: 1200px; height: 1200px; overflow: hidden; }
  body {
    background: var(--backdrop);
    font-family: "Montserrat", Arial, sans-serif;
    position: relative;
  }
  .card {
    position: absolute;
    left: 182px;
    width: 835px;
    height: 500px;
    background: var(--card);
    overflow: hidden;
  }
  .card--info { top: 80px; }
  .card--invite { top: 600px; }

  /* Info side */
  .chapel-mark {
    position: absolute;
    left: 62px; top: 190px;
    display: flex; align-items: center; gap: 14px;
  }
  .chapel-mark__square {
    width: 34px; height: 34px; background: var(--royal);
  }
  .chapel-mark__name {
    font-weight: 700; font-size: 30px; color: var(--royal); letter-spacing: 0.5px;
  }
  .chapel-name {
    position: absolute; left: 503px; top: 98px;
  }
  .chapel-name__main {
    font-weight: 700; font-size: 30px; color: var(--royal); letter-spacing: 0.3px; line-height: 1;
  }
  .chapel-name__sub {
    font-weight: 400; font-size: 18px; color: var(--ink); letter-spacing: 0.4px; margin-top: 6px;
  }
  .contact { position: absolute; left: 504px; list-style: none; }
  .contact__item {
    display: flex; align-items: center; height: 52px; margin-bottom: 9px;
  }
  .contact__icon { width: 52px; height: 52px; flex: none; }
  .contact__text {
    margin-left: 15px; font-size: 19px; color: var(--ink); line-height: 1.25;
  }
  .info-bands { position: absolute; left: 0; bottom: 0; }

  /* Invite side */
  .brand-name {
    position: absolute; left: 0; right: 0; top: 118px;
    text-align: center;
    font-weight: 800; font-size: 150px; color: var(--ink);
    letter-spacing: -2px; line-height: 1;
  }
  .invite-bands { position: absolute; left: 0; bottom: 0; }
  .welcome {
    position: absolute; left: 0; right: 0; top: 416px;
    text-align: center; color: var(--white);
    font-weight: 400; font-size: 24px; letter-spacing: 0.3px;
  }
</style>
</head>
<body>

<section class="card card--info">
  <div class="chapel-mark">
    <span class="chapel-mark__square"></span>
    <span class="chapel-mark__name">Morningbrook</span>
  </div>

  <div class="chapel-name">
    <div class="chapel-name__main">MORNINGBROOK</div>
    <div class="chapel-name__sub">RESTORATION CHAPEL</div>
  </div>

  <ul class="contact" style="top:202px">
    <li class="contact__item">
      <svg class="contact__icon" viewBox="0 0 52 52">
        <rect width="52" height="52" fill="var(--royal)"/>
        <polygon points="0,52 52,0 52,52" fill="var(--cyan)"/>
        <rect x="18" y="11" width="16" height="29" rx="2" fill="none" stroke="#fff" stroke-width="2"/>
        <circle cx="26" cy="35.5" r="1.5" fill="#fff"/>
      </svg>
      <span class="contact__text">555-017-3926</span>
    </li>
    <li class="contact__item">
      <svg class="contact__icon" viewBox="0 0 52 52">
        <rect width="52" height="52" fill="var(--royal)"/>
        <polygon points="0,52 52,0 52,52" fill="var(--cyan)"/>
        <g fill="none" stroke="#fff" stroke-width="1.8">
          <circle cx="26" cy="27" r="13"/>
          <ellipse cx="26" cy="27" rx="6" ry="13"/>
          <line x1="13" y1="27" x2="39" y2="27"/>
          <line x1="15" y1="20" x2="37" y2="20"/>
          <line x1="15" y1="34" x2="37" y2="34"/>
        </g>
      </svg>
      <span class="contact__text">www.mrcministry.example</span>
    </li>
    <li class="contact__item">
      <svg class="contact__icon" viewBox="0 0 52 52">
        <rect width="52" height="52" fill="var(--royal)"/>
        <polygon points="0,52 52,0 52,52" fill="var(--cyan)"/>
        <path d="M26 42 C19 32 16 27 16 22 A10 10 0 0 1 36 22 C36 27 33 32 26 42 Z" fill="#fff"/>
        <circle cx="26" cy="22" r="4" fill="var(--royal)"/>
      </svg>
      <span class="contact__text">1187 Tollgate Lane,<br>Decatur, GA, 30871</span>
    </li>
  </ul>

  <svg class="info-bands" width="835" height="72" viewBox="0 0 835 72">
    <rect x="0" y="29" width="835" height="43" fill="var(--cyan)"/>
    <polygon points="0,0 408,0 455,72 0,72" fill="var(--charcoal)"/>
  </svg>
</section>

<section class="card card--invite">
  <div class="brand-name">Zephra</div>

  <svg class="invite-bands" width="835" height="100" viewBox="0 0 835 100">
    <rect x="0" y="0" width="835" height="10" fill="var(--royal)"/>
    <rect x="0" y="10" width="835" height="90" fill="var(--charcoal)"/>
    <polygon points="218,0 613,0 642,57 193,57" fill="var(--cyan)"/>
  </svg>
  <div class="welcome">YOU'RE WELCOMED HERE</div>
</section>

</body>
</html>
```